Linewire Trade Journal Adverts

We need an advertisement design for our company 'Ember Ridge' www.emberridge-example.com
Ember Ridge is a telecommunication business that develop three different service. Cloud, Voice and Connectivity.
We are wanting to put an advertisement into Linewire Trade and would like the design, design that reflects our current brand and captures individual attention.
This advertisement needs to look professional and eye catching.
3 different advertisements are needed and I would like them to all be different yet link together in design so they can be recognised as Ember Ridge.
I have attached our logo below, along with the three advertisements.
Target Market(s)
Direct Reseller customers
Industry/Entity Type
Telecommunications
Requirements
Must have
- My project must follow our current branding that is on our website

```html
<!DOCTYPE html>
<html lang="en">
<head>
<meta charset="utf-8">
<title>Ember Ridge – Channel Partner Advert</title>
<link rel="stylesheet" href="https://fonts.googleapis.com/css2?family=Montserrat:wght@400;600;700;800&family=Arimo:wght@400;700&display=swap">
<style>
  :root {
    --page-bg: #ececec;
    --paper: #ffffff;
    --ink: #1e1e1e;
    --red: #e2232b;
    --deep-red: #c8161d;
    --pink: #e8116a;
    --orange: #f47a20;
    --amber: #f39a1e;
    --white: #ffffff;
    --soft-grey: #f3f3f3;
  }
  * { margin: 0; padding: 0; box-sizing: border-box; }
  html, body {
    width: 1200px; height: 2400px; overflow: hidden;
    background: var(--page-bg);
  }
  .canvas { position: relative; width: 1200px; height: 2400px; }
  .poster {
    position: absolute; left: 0; top: 420px;
    width: 1200px; height: 1560px;
    background: linear-gradient(180deg, var(--soft-grey) 0%, var(--paper) 30%, var(--paper) 100%);
    overflow: hidden;
    font-family: "Arimo", Arial, sans-serif;
  }
  .top-band {
    position: absolute; left: 0; top: 0; width: 100%; height: 12px;
    background: linear-gradient(90deg, var(--deep-red), var(--orange) 70%, var(--amber));
  }
  .headline {
    position: absolute; left: 0; top: 188px; width: 100%;
    text-align: center;
    font-family: "Montserrat", Arial, sans-serif;
    font-weight: 800; font-size: 38px; line-height: 48px;
    color: var(--ink); letter-spacing: 0.2px;
  }
  .headline .accent { color: var(--red); }
  .divider {
    position: absolute; left: 184px; top: 297px; width: 835px; height: 3px;
    background: var(--red);
  }
  .divider-mark {
    position: absolute; left: 558px; top: 291px; width: 86px; height: 14px;
    background: var(--deep-red);
  }
  .benefits { position: absolute; left: 0; top: 356px; width: 100%; }
  .benefit {
    position: absolute; width: 260px; text-align: center;
    font-family: "Arimo", Arial, sans-serif; font-weight: 700;
    font-size: 27px; line-height: 29px; color: var(--ink);
  }
  .benefit-icon {
    display: block; width: 146px; height: 146px; margin: 0 auto 18px;
  }
  .benefit--account { left: 195px; }
  .benefit--portal { left: 472px; }
  .benefit--billing { left: 748px; }

  .shape { position: absolute; left: 0; top: 0; width: 1200px; height: 1560px; }

  .pitch {
    position: absolute; left: 82px; top: 748px; width: 520px;
    color: var(--white);
    font-family: "Montserrat", Arial, sans-serif; font-weight: 700;
  }
  .pitch-lead { font-size: 32px; line-height: 44px; }
  .pitch-claim { font-size: 32px; line-height: 43px; }
  .pitch-figure { font-size: 44px; }
  .pitch-body {
    margin-top: 22px; width: 440px;
    font-family: "Arimo", Arial, sans-serif; font-weight: 400;
    font-size: 20px; line-height: 23px;
  }

  .contact {
    position: absolute; right: 143px; top: 1050px; width: 420px;
    text-align: right; color: var(--white);
    font-family: "Arimo", Arial, sans-serif;
  }
  .contact-cta {
    font-family: "Montserrat", Arial, sans-serif; font-weight: 800;
    font-size: 22px; line-height: 26px;
  }
  .contact-address { margin-top: 20px; font-size: 22px; line-height: 25px; }
  .contact-lines { margin-top: 22px; font-size: 21px; line-height: 29px; }
  .contact-lines .phone { font-weight: 700; }
  .brand-name {
    position: absolute; right: 143px; top: 1348px;
    font-family: "Montserrat", Arial, sans-serif; font-weight: 400;
    font-size: 58px; line-height: 70px; color: var(--white);
    letter-spacing: 1px; white-space: nowrap;
  }
</style>
</head>
<body>
<div class="canvas">
  <div class="poster">
    <div class="top-band"></div>

    <h1 class="headline">MOST CHANNEL PARTNERS <span class="accent">OFFER</span><br>THESE <span class="accent">BENEFITS</span> AS STANDARD:</h1>
    <div class="divider"></div>
    <div class="divider-mark"></div>

    <svg width="0" height="0" style="position:absolute">
      <defs>
        <linearGradient id="icon-stroke" x1="0" y1="0" x2="1" y2="1">
          <stop offset="0" stop-color="#f39a1e"/>
          <stop offset="1" stop-color="#e8116a"/>
        </linearGradient>
        <linearGradient id="icon-fill" x1="0" y1="0" x2="0" y2="1">
          <stop offset="0" stop-color="#f47a20"/>
          <stop offset="1" stop-color="#e2232b"/>
        </linearGradient>
      </defs>
    </svg>

    <div class="benefits">
      <div class="benefit benefit--account">
        <svg class="benefit-icon" viewBox="0 0 146 146" aria-hidden="true">
          <rect x="4" y="4" width="138" height="138" rx="20" fill="#fff" stroke="url(#icon-stroke)" stroke-width="5"/>
          <circle cx="73" cy="40" r="9" fill="url(#icon-fill)"/>
          <path d="M59 66 a14 12 0 0 1 28 0 z" fill="url(#icon-fill)"/>
          <circle cx="42" cy="86" r="9" fill="url(#icon-fill)"/>
          <path d="M28 112 a14 12 0 0 1 28 0 z" fill="url(#icon-fill)"/>
          <circle cx="104" cy="86" r="9" fill="url(#icon-fill)"/>
          <path d="M90 112 a14 12 0 0 1 28 0 z" fill="url(#icon-fill)"/>
          <path d="M52 56 Q40 64 40 74 M94 56 Q106 64 106 74 M60 104 L86 104" fill="none" stroke="url(#icon-fill)" stroke-width="3"/>
        </svg>
        Account<br>management
      </div>
      <div class="benefit benefit--portal">
        <svg class="benefit-icon" viewBox="0 0 146 146" aria-hidden="true">
          <rect x="4" y="4" width="138" height="138" rx="20" fill="#fff" stroke="url(#icon-stroke)" stroke-width="5"/>
          <g fill="none" stroke="url(#icon-fill)" stroke-width="5">
            <circle cx="66" cy="76" r="34"/>
            <ellipse cx="66" cy="76" rx="14" ry="34"/>
            <line x1="32" y1="76" x2="100" y2="76"/>
            <path d="M37 58 H95 M37 94 H95"/>
          </g>
          <rect x="88" y="42" width="30" height="24" rx="3" fill="url(#icon-fill)"/>
          <path d="M94 42 v-7 a9 9 0 0 1 18 0 v7" fill="none" stroke="url(#icon-fill)" stroke-width="4"/>
        </svg>
        A secure<br>portal
      </div>
      <div class="benefit benefit--billing">
        <svg class="benefit-icon" viewBox="0 0 146 146" aria-hidden="true">
          <rect x="4" y="4" width="138" height="138" rx="20" fill="#fff" stroke="url(#icon-stroke)" stroke-width="5"/>
          <circle cx="73" cy="40" r="14" fill="none" stroke="url(#icon-fill)" stroke-width="4"/>
          <path d="M73 32 v16 M68 36 h8 M68 44 h8" stroke="url(#icon-fill)" stroke-width="3"/>
          <g fill="none" stroke="url(#icon-fill)" stroke-width="4">
            <path d="M32 82 L78 66 L104 84 L58 100 Z"/>
            <path d="M32 92 L58 110 L104 94"/>
            <path d="M32 102 L58 120 L104 104"/>
          </g>
          <path d="M92 108 q14 -6 24 4 l-10 10 z" fill="url(#icon-fill)"/>
        </svg>
        An automated<br>billing engine
      </div>
    </div>

    <svg class="shape" viewBox="0 0 1200 1560" aria-hidden="true">
      <defs>
        <linearGradient id="left-fill" x1="0" y1="0" x2="0" y2="1">
          <stop offset="0" stop-color="#e2232b"/>
          <stop offset="0.65" stop-color="#e3173b"/>
          <stop offset="1" stop-color="#e8116a"/>
        </linearGradient>
      </defs>
      <path d="M0 672 C110 610 330 596 460 642 C560 690 596 860 590 1020 L318 1541 L0 1212 Z" fill="url(#left-fill)"/>
    </svg>

    <svg class="shape" viewBox="0 0 1200 1560" role="img" aria-label="Photograph of a businessman working at a laptop in an office, tinted in orange and red">
      <defs>
        <linearGradient id="right-fill" x1="0.3" y1="0" x2="0.6" y2="1">
          <stop offset="0" stop-color="#f68a26"/>
          <stop offset="0.4" stop-color="#f0612a"/>
          <stop offset="0.75" stop-color="#e4263a"/>
          <stop offset="1" stop-color="#e5125c"/>
        </linearGradient>
      </defs>
      <path d="M452 1560 L886 806 C930 720 980 630 1060 602 C1130 584 1180 610 1200 640 L1200 1560 Z" fill="url(#right-fill)"/>
    </svg>

    <div class="pitch">
      <p class="pitch-lead">But what about</p>
      <p class="pitch-claim"><span class="pitch-figure">£2m</span> additional<br>revenue in only 12<br>months? There’s<br>nothing standard<br>about that…</p>
      <p class="pitch-body">We’ll supercharge your business with secure cloud-first voice, network and storage solutions that enable your clients – and you – to thrive.</p>
    </div>

    <div class="contact">
      <p class="contact-cta">TALK TO US<br>ABOUT YOUR<br>PARTNER POTENTIAL</p>
      <p class="contact-address">The Foundry,<br>Kestrel Close,<br>Kestrel Business Park,<br>Hadley, HD9 4QZ</p>
      <p class="contact-lines"><span class="phone">T: 0300 555 0148</span><br>E: info@emberridge-example.com</p>
    </div>

    <div class="brand-name">EMBER RIDGE</div>
  </div>
</div>
</body>
</html>
```